Emergency Medical Training and Events Company Business Needs Business Card Design

We are in need of a business card for our dynamic company expanding its customer base and need to be easily contacted and identified for when we visit with government officials, potential EMS / Fire agencies and county coordinators to arrange for training programs for first responders to better prepare them for critical thinking at critical incidents.

Target Market(s)

EMS/Fire and Event Promoters

Industry/Entity Type

Medical

Contact Information for Business Card

Two cards, comparable designs:

Martin K. Halvey, Principal, m.halvey@rvqtlo.com
Owen Tash, Event and Training Specialist, o.tash@rvqtlo.com

Font styles to use
Other font styles liked:
• Cambria

Colors

Designer to choose colors to be used in the design.

Requirements
Must have
• Company Logo, Spots for Name, Title, Phone Number, Email, Website
• A bullet list stating that we offer, QRB CPR and First Aid Instructors, Hold the Line Instructors, Event EMS, CME's, MCI Training and Planning. We prefer to have a black background for the card but if you can make a blue or white card stand out we would review that as well.
Should not have
• Tacky logos or special sayings ... simple, elegant, professional is the look we seek

```html
<!DOCTYPE html>
<html lang="en">
<head>
<meta charset="utf-8">
<title>Rivertide Response — Business Cards</title>
<link href="https://fonts.googleapis.com/css2?family=Merriweather:wght@400;700&family=Montserrat:wght@700;800&display=swap" rel="stylesheet">
<style>
  :root {
    --canvas: #f3f3f3;
    --navy: #182058;
    --navy-light: #1f3590;
    --glow: #2f63d8;
    --red: #c41014;
    --white: #ffffff;
    --ink: #1b2260;
  }
  * { box-sizing: border-box; margin: 0; padding: 0; }
  html, body { width: 1200px; height: 1200px; overflow: hidden; }
  body {
    background: radial-gradient(ellipse at 30% 20%, #fafafa 0%, var(--canvas) 60%, #eeeeee 100%);
    position: relative;
    font-family: "Merriweather", Georgia, serif;
  }
  .label {
    position: absolute;
    width: 226px; height: 37px;
    border-radius: 19px;
    background: var(--red);
    color: var(--white);
    font-family: "Montserrat", Arial, sans-serif;
    font-weight: 800;
    font-size: 15px;
    letter-spacing: 3px;
    display: flex; align-items: center; justify-content: center;
  }
  .card {
    position: absolute;
    width: 440px; height: 252px;
    border-radius: 31px;
    background: var(--navy);
    overflow: hidden;
    box-shadow: 0 4px 6px rgba(0,0,0,0.28);
    color: var(--white);
  }
  .card-texture {
    position: absolute; inset: 0;
    background:
      radial-gradient(circle at 0% 0%, rgba(47,99,216,0.75) 0%, rgba(31,53,144,0.45) 30%, rgba(24,32,88,0) 60%),
      radial-gradient(circle at 0% 80%, rgba(47,99,216,0.4) 0%, rgba(24,32,88,0) 40%);
  }
  .card-back .card-texture {
    background: radial-gradient(circle at 0% 40%, rgba(47,99,216,0.3) 0%, rgba(24,32,88,0) 45%);
  }
  .brand-block {
    position: absolute; left: 60px; top: 62px;
    width: 120px; height: 130px;
    display: flex; flex-direction: column; align-items: center; justify-content: center; gap: 10px;
  }
  .brand-dot { width: 52px; height: 52px; border-radius: 50%; background: var(--red); }
  .brand-name {
    font-weight: 700; font-size: 13px; line-height: 1.3; text-align: center; color: var(--white);
  }
  .accent-bar { position: absolute; left: 220px; top: 60px; width: 13px; height: 3px; background: var(--red); }
  .person-name { position: absolute; left: 220px; top: 68px; font-weight: 700; font-size: 21px; white-space: nowrap; }
  .person-title { position: absolute; left: 219px; top: 103px; font-weight: 700; font-size: 7.5px; letter-spacing: 1.8px; white-space: nowrap; }
  .contact { position: absolute; left: 219px; display: flex; align-items: center; gap: 8px; font-size: 10px; letter-spacing: 0.3px; }
  .contact svg { width: 12px; height: 12px; flex: none; }
  .contact-email { top: 135px; }
  .contact-phone { top: 154px; }
  .back-brand {
    position: absolute; left: 0; right: 0; top: 98px;
    display: flex; align-items: center; justify-content: center; gap: 12px;
  }
  .back-brand .brand-dot { width: 40px; height: 40px; }
  .back-brand .brand-name { font-size: 22px; text-align: left; white-space: nowrap; }
  .web-tab { position: absolute; left: 116px; bottom: 0; width: 208px; height: 27px; }
  .web-tab svg { position: absolute; inset: 0; }
  .web-address {
    position: absolute; inset: 0; display: flex; align-items: center; justify-content: center;
    color: var(--ink); font-size: 10px; letter-spacing: 2.4px; padding-top: 2px;
  }
</style>
</head>
<body>
  <div class="label" style="left:247px; top:257px;">BIZCARD FRONT</div>
  <div class="label" style="left:727px; top:257px;">BIZCARD FRONT</div>

  <section class="card card-front" style="left:140px; top:330px;">
    <div class="card-texture" role="img" aria-label="Faint glowing blue hexagon network pattern"></div>
    <div class="brand-block"><span class="brand-dot"></span><span class="brand-name">Rivertide<br>Response</span></div>
    <span class="accent-bar"></span>
    <h1 class="person-name">Martin K. Halvey</h1>
    <p class="person-title">Principal</p>
    <p class="contact contact-email"><svg viewBox="0 0 12 12"><rect x="0.5" y="2" width="11" height="8" rx="1" fill="#fff"/><path d="M1 3 L6 7 L11 3" stroke="#182058" stroke-width="1.2" fill="none"/></svg>m.halvey@rvqtlo.com</p>
    <p class="contact contact-phone"><svg viewBox="0 0 12 12"><circle cx="6" cy="6" r="6" fill="#fff"/><path d="M4 3.2 L5 4.8 L4.5 5.5 Q5.3 7 6.6 7.5 L7.3 7 L8.8 8 L8.2 9 Q5.5 9 3.2 5 Q3.2 3.8 4 3.2Z" fill="#182058"/></svg>555.014.2290</p>
  </section>

  <section class="card card-front" style="left:620px; top:330px;">
    <div class="card-texture" role="img" aria-label="Faint glowing blue hexagon network pattern"></div>
    <div class="brand-block"><span class="brand-dot"></span><span class="brand-name">Rivertide<br>Response</span></div>
    <span class="accent-bar"></span>
    <h1 class="person-name" style="top:71px;">Owen Tash</h1>
    <p class="person-title">Event and Training Specialist</p>
    <p class="contact contact-email"><svg viewBox="0 0 12 12"><rect x="0.5" y="2" width="11" height="8" rx="1" fill="#fff"/><path d="M1 3 L6 7 L11 3" stroke="#182058" stroke-width="1.2" fill="none"/></svg>o.tash@rvqtlo.com</p>
    <p class="contact contact-phone"><svg viewBox="0 0 12 12"><circle cx="6" cy="6" r="6" fill="#fff"/><path d="M4 3.2 L5 4.8 L4.5 5.5 Q5.3 7 6.6 7.5 L7.3 7 L8.8 8 L8.2 9 Q5.5 9 3.2 5 Q3.2 3.8 4 3.2Z" fill="#182058"/></svg>555.014.2290</p>
  </section>

  <section class="card card-back" style="left:140px; top:618px;">
    <div class="card-texture" role="img" aria-label="Faint dark blue hexagon network pattern"></div>
    <div class="back-brand"><span class="brand-dot"></span><span class="brand-name">Rivertide Response</span></div>
    <div class="web-tab">
      <svg viewBox="0 0 208 27" preserveAspectRatio="none"><path d="M0 27 C14 27 18 0 36 0 L172 0 C190 0 194 27 208 27 Z" fill="#fff"/></svg>
      <span class="web-address">www.rvqtlo.com</span>
    </div>
  </section>

  <section class="card card-back" style="left:620px; top:618px;">
    <div class="card-texture" role="img" aria-label="Faint dark blue hexagon network pattern"></div>
    <div class="back-brand"><span class="brand-dot"></span><span class="brand-name">Rivertide Response</span></div>
    <div class="web-tab">
      <svg viewBox="0 0 208 27" preserveAspectRatio="none"><path d="M0 27 C14 27 18 0 36 0 L172 0 C190 0 194 27 208 27 Z" fill="#fff"/></svg>
      <span class="web-address">www.rvqtlo.com</span>
    </div>
  </section>

  <div class="label" style="left:247px; top:906px;">BIZCARD BACK</div>
  <div class="label" style="left:727px; top:906px;">BIZCARD BACK</div>
</body>
</html>
```